Corporate A4 Advert for Worldwide Timber Trader/Agent

We need a new professional company ad, which will be used in worldwide magazine publications. something sophisticated.
Our website - www.qrolumber.co.uk - for info. We are timber agents and sell timber from one part of the world to another.
I will upload a selection of product photos to include - suggest using not all but a selection of some them, to showcase the product. Our buyers purchase both logs and sawn timber
We would like this ad to list our source areas and product groups.
Our company colour is British Racing Green
Updates

Target Market(s)

timber buyers

Industry/Entity Type

Timber

Colors
00AB8E
00BBA5
67D7C9
C6EFE9
E9F9F6

Requirements
Must have
• company logo

```html
<!DOCTYPE html>
<html lang="en">
<head>
<meta charset="utf-8">
<title>QRO Lumber – World Hardwoods &amp; Clear Softwoods Advert</title>
<link rel="stylesheet" href="https://fonts.googleapis.com/css2?family=Montserrat:wght@600;700;800&family=Raleway:wght@500&family=Open+Sans:wght@400;500&display=swap">
<style>
  :root{
    --page-bg:#c4c4c4;
    --paper:#ffffff;
    --ink:#262b27;
    --teal:#0aa98b;
    --mint:#c6efe9;
    --aqua:#67d7c9;
    --racing-green:#004225;
    --sage:#6ea688;
    --band-top:#4f7b77;
    --band-mid:#658d84;
    --earth:#6e5a32;
    --white:#ffffff;
  }
  *{box-sizing:border-box;margin:0;padding:0}
  html,body{width:1200px;height:1200px;overflow:hidden;background:var(--page-bg)}
  .advert{
    position:absolute;left:190px;top:20px;width:821px;height:1160px;
    background:var(--paper);overflow:hidden;
  }
  .lower-band{
    position:absolute;left:0;top:588px;width:100%;height:572px;
    background:linear-gradient(180deg,var(--band-top) 0%,var(--band-mid) 48%,#6f7f63 66%,#7a6a43 80%,var(--earth) 100%);
  }
  .kicker{
    position:absolute;left:38px;top:70px;
    font:500 31px/1 'Raleway',sans-serif;color:#3d403e;letter-spacing:-.2px;
  }
  .headline{
    position:absolute;left:36px;top:112px;
    font:800 64px/57px 'Montserrat',sans-serif;color:var(--ink);letter-spacing:-1.5px;
    text-transform:uppercase;
  }
  .headline .accent{color:var(--teal)}
  .intro{
    position:absolute;left:38px;top:360px;width:420px;
    font:400 19.5px/26px 'Open Sans',sans-serif;color:#1f2220;
  }
  .pointer-arrow{position:absolute;left:462px;top:346px;width:78px;height:74px}
  .hero-ring{
    position:absolute;left:515px;top:43px;width:382px;height:382px;border-radius:50%;
    background:var(--ink);
  }
  .hero-ring .gap{
    position:absolute;inset:19px;border-radius:50%;background:var(--paper);
  }
  .hero-photo{
    position:absolute;inset:25px;border-radius:50%;
    background:linear-gradient(180deg,#9fbfe0 0%,#b9cfe0 30%,#4e5e3a 48%,#c87a42 70%,#d0733a 100%);
  }
  .product-card{
    position:absolute;top:452px;width:333px;height:209px;background:#fbfbf7;padding:12px;
    box-shadow:0 4px 10px rgba(0,0,0,.18);
  }
  .product-card.logs{left:61px}
  .product-card.sawn{left:425px}
  .product-photo{position:relative;width:100%;height:100%}
  .logs .product-photo{background:linear-gradient(180deg,#6c8a6a 0%,#b56a3b 35%,#a85a30 70%,#2e3e38 100%)}
  .sawn .product-photo{background:linear-gradient(180deg,#c5c0b8 0%,#b8633a 25%,#a3502d 65%,#2e3e38 100%)}
  .product-label{
    position:absolute;left:18px;bottom:6px;
    font:500 24px/1 'Raleway',sans-serif;color:var(--white);letter-spacing:.3px;
  }
  .list-heading{
    position:absolute;top:686px;
    font:700 26px/1 'Montserrat',sans-serif;color:var(--white);
  }
  .list-heading.areas{left:56px}
  .list-heading.products{left:366px}
  .divider{position:absolute;left:325px;top:692px;width:1.5px;height:205px;background:rgba(255,255,255,.8)}
  .bullet-list{position:absolute;top:724px;list-style:none}
  .bullet-list li{
    display:flex;align-items:center;gap:8px;height:23.3px;
    font:400 17.5px/1 'Open Sans',sans-serif;color:var(--white);white-space:nowrap;
  }
  .bullet-list svg{width:15px;height:15px;flex:none}
  .list-areas{left:56px}
  .list-products-a{left:366px}
  .list-products-b{left:590px}
  .yard-scene{
    position:absolute;left:0;top:880px;width:100%;height:280px;
    background:linear-gradient(180deg,rgba(70,90,70,0) 0%,rgba(60,70,50,.35) 35%,rgba(120,95,55,.25) 60%,rgba(95,75,40,.3) 100%);
  }
  .corner-halo{
    position:absolute;left:-115px;top:875px;width:384px;height:384px;border-radius:50%;
    background:var(--sage);opacity:.85;
  }
  .corner-ring{
    position:absolute;left:-88px;top:902px;width:330px;height:330px;border-radius:50%;
    background:var(--racing-green);
  }
  .corner-ring .gap{position:absolute;inset:14px;border-radius:50%;background:var(--paper)}
  .corner-photo{
    position:absolute;inset:19px;border-radius:50%;
    background:linear-gradient(180deg,#c9cfd2 0%,#9aa3a0 28%,#c2683c 55%,#a9552f 80%,#8a4a2c 100%);
  }
  .brand-name{
    position:absolute;left:560px;top:988px;width:140px;text-align:center;
    font:800 42px/1 'Montserrat',sans-serif;color:var(--white);letter-spacing:1px;
  }
  .phone{
    position:absolute;left:476px;top:1042px;display:flex;align-items:center;gap:9px;
    font:700 28px/1 'Montserrat',sans-serif;color:var(--white);
  }
  .phone svg{width:21px;height:21px}
  .web{
    position:absolute;left:501px;top:1088px;width:252px;height:29px;border:2px solid var(--aqua);
    border-radius:15px;display:flex;align-items:center;justify-content:center;
    font:400 19px/1 'Open Sans',sans-serif;color:var(--white);
  }
</style>
</head>
<body>
<svg width="0" height="0" style="position:absolute">
  <symbol id="corner-arrow" viewBox="0 0 16 16">
    <path d="M3 2.5H13.5V13" fill="none" stroke="currentColor" stroke-width="2.6"/>
    <path d="M13 3L3 13" stroke="currentColor" stroke-width="2.6"/>
  </symbol>
</svg>

<main class="advert">
  <div class="lower-band"></div>
  <div class="yard-scene" role="img" aria-label="Timber yard with open sheds and forest edge under a hazy sky"></div>

  <p class="kicker">The Natural Source of</p>
  <h1 class="headline">World<br>Hardwoods<br><span class="accent">&amp; Clear<br>Softwoods</span></h1>
  <p class="intro">We take pride in trading timber globally and responsibly. Developing and nurturing clients and suppliers is critical to our success.</p>

  <svg class="pointer-arrow" viewBox="0 0 78 74" aria-hidden="true">
    <path d="M0 6H72V74" fill="none" stroke="var(--mint)" stroke-width="11"/>
    <path d="M70 8L22 56" stroke="var(--mint)" stroke-width="11"/>
  </svg>

  <div class="hero-ring">
    <div class="gap"></div>
    <div class="hero-photo" role="img" aria-label="Logging truck loaded with large logs on a red earth clearing beside tropical forest"></div>
  </div>

  <figure class="product-card logs">
    <div class="product-photo" role="img" aria-label="Stack of large hardwood logs">
      <figcaption class="product-label">LOGS</figcaption>
    </div>
  </figure>
  <figure class="product-card sawn">
    <div class="product-photo" role="img" aria-label="Strapped bundle of sawn hardwood planks">
      <figcaption class="product-label">SAWN TIMBER</figcaption>
    </div>
  </figure>

  <h2 class="list-heading areas">Source of Areas</h2>
  <ul class="bullet-list list-areas">
    <li><svg style="color:var(--mint)"><use href="#corner-arrow"/></svg>Africa</li>
    <li><svg style="color:var(--mint)"><use href="#corner-arrow"/></svg>Far East</li>
    <li><svg style="color:var(--mint)"><use href="#corner-arrow"/></svg>South America</li>
    <li><svg style="color:var(--mint)"><use href="#corner-arrow"/></svg>North America</li>
    <li><svg style="color:var(--mint)"><use href="#corner-arrow"/></svg>Europe</li>
  </ul>

  <div class="divider"></div>

  <h2 class="list-heading products">Our Products</h2>
  <ul class="bullet-list list-products-a">
    <li><svg style="color:var(--mint)"><use href="#corner-arrow"/></svg>Hardwoods</li>
    <li><svg style="color:var(--mint)"><use href="#corner-arrow"/></svg>Softwood</li>
    <li><svg style="color:var(--mint)"><use href="#corner-arrow"/></svg>Logs</li>
    <li><svg style="color:var(--mint)"><use href="#corner-arrow"/></svg>Semi-Finished Products</li>
    <li><svg style="color:var(--mint)"><use href="#corner-arrow"/></svg>Douglas Fir</li>
    <li><svg style="color:var(--mint)"><use href="#corner-arrow"/></svg>Hemlock</li>
    <li><svg style="color:var(--mint)"><use href="#corner-arrow"/></svg>Southern Yellow</li>
  </ul>
  <ul class="bullet-list list-products-b">
    <li><svg style="color:var(--mint)"><use href="#corner-arrow"/></svg>Logs</li>
    <li><svg style="color:var(--mint)"><use href="#corner-arrow"/></svg>Boules</li>
    <li><svg style="color:var(--mint)"><use href="#corner-arrow"/></svg>Decking</li>
    <li><svg style="color:var(--mint)"><use href="#corner-arrow"/></svg>Laminations</li>
    <li><svg style="color:var(--mint)"><use href="#corner-arrow"/></svg>Sauna Laths</li>
    <li><svg style="color:var(--mint)"><use href="#corner-arrow"/></svg>Pine</li>
    <li><svg style="color:var(--mint)"><use href="#corner-arrow"/></svg>Western Red Cedar</li>
  </ul>

  <div class="corner-halo"></div>
  <div class="corner-ring">
    <div class="gap"></div>
    <div class="corner-photo" role="img" aria-label="Yard worker marking stacked sawn timber outside a sawmill"></div>
  </div>

  <div class="brand-name">QRO</div>

  <div class="phone">
    <svg viewBox="0 0 24 24" aria-hidden="true">
      <circle cx="12" cy="12" r="10.5" fill="none" stroke="var(--aqua)" stroke-width="1.6"/>
      <path d="M8.3 6.5l2 2.2-1.2 1.5c.8 1.8 2 3 3.7 3.8l1.5-1.2 2.2 2-1.3 2c-4.2-.3-8.3-4.4-8.6-8.6z" fill="var(--aqua)"/>
    </svg>
    <span>+44(0)20 7946 0321</span>
  </div>
  <div class="web">www.qrolumber.co.uk</div>
</main>
</body>
</html>
```